Soy Candle Business needs a label design

We need a label design for a new company selling soy candles - Velvet Hearth Studio.

We are using apothecary jars in 3 sizes.
As per attached candles will be dressed with a beautiful black bow and all finished with a diamante in centre of bow.

We would like label done on lid of candle jars - 5cm circle (5cm from one side to the other), this way one label will fit each product size. Label will be done as a sticker.

We are thinking of the background colour to be black, however are open to recommendations. We want label to be classy, elegant and simple.

Inspiration for candle design came from attached invitation that features the bow, and beautiful vintage paper on top area.

Label should include the following 3 pieces of information:
Velvet Hearth Studio (company name)
Coconut Lime (this will change depending on fragrance)
Soy Candle

Velvet Hearth Studio does not have a company logo... what is done for the label will set tone for what is done across other elements of business moving forward.

Industry/Entity Type

Business

Requirements
Must have
• Velvet Hearth Studio
Fragrance Flavour
Soy Candle

```html
<!DOCTYPE html>
<html lang="en">
<head>
<meta charset="utf-8">
<title>Velvet Hearth Studio – Coconut Lime Soy Candle Label</title>
<link rel="stylesheet" href="https://fonts.googleapis.com/css2?family=Dancing+Script:wght@500&family=Cormorant+Garamond:wght@500&display=swap">
<style>
  :root {
    --paper: #ffffff;
    --label-black: #12110f;
    --mint: #6cbf98;
    --mint-deep: #3f7d61;
    --butter: #f6ec8c;
  }
  html, body {
    margin: 0;
    padding: 0;
    width: 1200px;
    height: 927px;
    overflow: hidden;
    background: var(--paper);
  }
  .canvas {
    display: block;
    width: 1200px;
    height: 927px;
  }
  .label-rim { fill: var(--mint); }
  .label-face { fill: var(--label-black); }
  .flourish-panel { fill: url(#flourishTone); }
  .studio-name {
    font-family: "Dancing Script", cursive;
    font-size: 44px;
    fill: var(--butter);
    letter-spacing: 0.5px;
  }
  .fragrance-name {
    font-family: "Dancing Script", cursive;
    font-size: 88px;
    fill: var(--mint);
  }
  .product-type {
    font-family: "Cormorant Garamond", serif;
    font-size: 30px;
    fill: var(--butter);
    letter-spacing: 1px;
  }
</style>
</head>
<body>
<svg class="canvas" viewBox="0 0 1200 927" xmlns="http://www.w3.org/2000/svg">
  <defs>
    <radialGradient id="flourishTone" cx="50%" cy="50%" r="50%">
      <stop offset="0%" stop-color="#3f7d61"/>
      <stop offset="100%" stop-color="#6cbf98"/>
    </radialGradient>
    <clipPath id="upperFlourishClip"><rect x="0" y="0" width="1200" height="418"/></clipPath>
    <clipPath id="lowerFlourishClip"><rect x="0" y="522" width="1200" height="405"/></clipPath>
    <path id="arcTop" d="M 408 463 A 192 192 0 0 1 792 463"/>
    <path id="arcBottom" d="M 340 463 A 260 260 0 0 0 860 463"/>
  </defs>

  <g class="candle-label">
    <circle class="label-rim" cx="600" cy="463" r="262"/>
    <circle class="label-face" cx="600" cy="463" r="252"/>

    <circle class="flourish-panel" cx="604" cy="462" r="176" clip-path="url(#upperFlourishClip)"
            role="img" aria-label="Swirling vine and leaf flourish ornament in mint green, upper half"/>
    <circle class="flourish-panel" cx="604" cy="462" r="176" clip-path="url(#lowerFlourishClip)"
            role="img" aria-label="Swirling vine and leaf flourish ornament in mint green, lower half"/>

    <text class="studio-name">
      <textPath href="#arcTop" startOffset="50%" text-anchor="middle">Velvet Hearth Studio</textPath>
    </text>

    <text class="fragrance-name" x="602" y="500" text-anchor="middle">Coconut Lime</text>

    <g transform="translate(0 -40)">
      <text class="product-type">
        <textPath href="#arcBottom" startOffset="50%" text-anchor="middle">SOY CANDLE</textPath>
      </text>
    </g>
  </g>
</svg>
</body>
</html>
```